Release Therapy business card that deals with the release of negative issues

I need a business card for my business called PEBBLES (A warm hearth to rest when you tire) ... I'm a therapist that deals with people releasing negative issues, by applying therapies that incorporate, hypnosis, aromatherapy and listen therapy..I like the colour green and soft blues...My idea is for a hand releasing butterflies, and incorporating soft clouds....
Target Market(s)
All people, all ages
Industry/Entity Type
Business
Contact Information for Business Card
PEBBLES"A Warm Hearth To Rest When You Tire"Yvette R BrockingtonRelease Therapist0411 743 781email: calmingpaths4you@quietmail.example
Requirements
Must have
- butterflies and soft clouds
Nice to have
- I like the decorative and script fonts for business name, and also my name
- Marisol T Fenwhistle...

```html
<!DOCTYPE html>
<html lang="en">
<head>
<meta charset="utf-8">
<title>PEBBLES – Business Card</title>
<link rel="stylesheet" href="https://fonts.googleapis.com/css2?family=Ubuntu:wght@400;700&family=Dancing+Script:wght@600&display=swap">
<style>
  :root {
    --stage: #ece8e1;
    --sky-light: #b4dde4;
    --sky-deep: #6cb8c6;
    --cloud-white: rgba(246, 248, 249, 0.85);
    --cloud-blue: rgba(63, 143, 208, 0.55);
    --paper-light: #f1f1ef;
    --paper-shade: #d9d9d4;
    --name-olive: #8b8a72;
    --label-grey: #9a9a90;
    --contact-teal: #1f5f78;
    --wing-orange: rgba(232, 162, 58, 0.55);
    --shadow: rgba(60, 50, 40, 0.22);
  }
  * { box-sizing: border-box; margin: 0; padding: 0; }
  html, body {
    width: 1200px; height: 864px; overflow: hidden;
    background: var(--stage);
  }
  .canvas {
    position: relative; width: 1200px; height: 864px;
    display: flex; align-items: center; justify-content: center; gap: 60px;
  }
  .card {
    position: relative; width: 500px; height: 290px;
    border-radius: 22px; overflow: hidden;
    box-shadow: 0 14px 30px var(--shadow);
  }

  /* Front */
  .card--front {
    background: linear-gradient(160deg, var(--sky-light) 0%, var(--sky-deep) 100%);
  }
  .brand {
    position: absolute; left: 0; right: 0; top: 92px;
    text-align: center;
    font-family: "Ubuntu", sans-serif; font-weight: 700;
    font-size: 64px; letter-spacing: 2px; color: #ffffff;
  }
  .tagline {
    position: absolute; left: 0; right: 0; top: 170px;
    text-align: center;
    font-family: "Dancing Script", cursive; font-weight: 600;
    font-size: 21px; color: #ffffff;
  }
  .paper-plane-art {
    position: absolute; left: 26px; top: 212px; width: 70px; height: 50px;
    background: radial-gradient(ellipse at center, rgba(255,255,255,0.3) 0%, rgba(255,255,255,0) 70%);
  }
  .cloud-art {
    position: absolute;
    background: radial-gradient(ellipse at center, var(--cloud-white) 0%, var(--cloud-blue) 45%, rgba(63,143,208,0) 72%);
  }
  .cloud-art--corner { right: -20px; top: -10px; width: 150px; height: 130px; }
  .cloud-art--low { left: 250px; bottom: -30px; width: 190px; height: 110px; }

  /* Back */
  .card--back {
    background: linear-gradient(160deg, var(--paper-light) 0%, var(--paper-shade) 100%);
    font-family: "Ubuntu", sans-serif;
  }
  .butterfly-art {
    position: absolute; right: 22px; top: 18px; width: 70px; height: 44px;
    background: radial-gradient(ellipse at center, var(--wing-orange) 0%, rgba(232,162,58,0) 70%);
  }
  .holder-name {
    position: absolute; left: 48px; top: 78px;
    font-size: 34px; font-weight: 700; color: var(--name-olive);
  }
  .holder-role {
    position: absolute; left: 250px; top: 126px;
    font-size: 17px; font-weight: 400; color: var(--label-grey);
  }
  .contact {
    position: absolute; left: 110px; top: 168px;
    display: grid; grid-template-columns: 64px auto; row-gap: 14px; align-items: baseline;
  }
  .contact__label { font-size: 13px; color: var(--label-grey); }
  .contact__value { color: var(--contact-teal); }
  .contact__value--phone { font-size: 22px; }
  .contact__value--email { font-size: 15px; }
</style>
</head>
<body>
<main class="canvas">
  <section class="card card--front" aria-label="Business card front">
    <div class="cloud-art cloud-art--corner" role="img" aria-label="White and blue cartoon clouds in the corner"></div>
    <div class="cloud-art cloud-art--low" role="img" aria-label="White and blue cartoon clouds along the lower edge"></div>
    <div class="paper-plane-art" role="img" aria-label="Line drawing of a paper plane with a dashed flight path"></div>
    <h1 class="brand">PEBBLES</h1>
    <p class="tagline">A Warm Hearth To Rest When You Tire</p>
  </section>

  <section class="card card--back" aria-label="Business card back">
    <div class="butterfly-art" role="img" aria-label="Orange monarch butterfly resting on the corner"></div>
    <h2 class="holder-name">Marisol T Fenwhistle</h2>
    <p class="holder-role">Therapist</p>
    <dl class="contact">
      <dt class="contact__label">Call</dt>
      <dd class="contact__value contact__value--phone">0482 516 904</dd>
      <dt class="contact__label">email</dt>
      <dd class="contact__value contact__value--email">calmingpaths4you@quietmail.example</dd>
    </dl>
  </section>
</main>
</body>
</html>
```